Signage for Multi-family Veterans Housing community

Need a design concept package for the above. Need Historic feel design logo element together with "Ashcombe Veterans Village"in serif font, for a Veterans (retired military) Affordable Housing community, in the historic town of Windsor, California USA. I have attached an architectural drawing of the future housing community, that will need the signage. Also, attached are photos of the town of Windsor signage, for the historic downtown vibe, do not use the sign elements. Please include in the concept package a community ID sign similar to the craftsman community ID sign attached. The community ID sign will have the logo with name and address only, use a placeholder for Address. Thank you

Font styles to use
Serif
Sans Serif

Requirements
Should not have
• Please no American flags or other military references. Other than the word “I Veterans” in the title.

```html
<!DOCTYPE html>
<html lang="en">
<head>
<meta charset="utf-8">
<title>Ashcombe Veterans Village – Poster</title>
<link rel="stylesheet" href="https://fonts.googleapis.com/css2?family=Marcellus&family=Libre+Baskerville:wght@700&display=swap">
<style>
  :root {
    --backdrop: #3b3b3d;
    --stripe-light: #eef6fa;
    --stripe-blue: #d4e9f2;
    --title-blue: #6aafc6;
    --body-blue: #5c9fb6;
    --rule-blue: #78b6cb;
    --scene-sky: #e6f2f7;
    --scene-roof: #8a6a55;
    --scene-wall: #b9b8a6;
    --scene-tree: #56704a;
    --scene-ground: #7d7a72;
  }
  * { margin: 0; padding: 0; box-sizing: border-box; }
  html, body {
    width: 855px;
    height: 1200px;
    overflow: hidden;
    background: var(--backdrop);
  }
  .poster {
    position: absolute;
    left: 100px;
    top: 100px;
    width: 655px;
    height: 1000px;
    overflow: hidden;
    background: repeating-linear-gradient(
      90deg,
      var(--stripe-light) 0 28px,
      var(--stripe-blue) 28px 56px
    );
  }
  .poster-title {
    position: absolute;
    top: 120px;
    left: 0;
    width: 100%;
    text-align: center;
    font-family: "Marcellus", serif;
    color: var(--title-blue);
    line-height: 1;
  }
  .poster-title .name {
    display: block;
    font-size: 98px;
    letter-spacing: 3px;
  }
  .poster-title .tagline {
    display: block;
    margin-top: 14px;
    font-size: 50px;
    font-weight: 700;
  }
  .rule {
    position: absolute;
    left: 129px;
    width: 405px;
    height: 3px;
    background: var(--rule-blue);
  }
  .rule.top { top: 376px; }
  .rule.bottom { top: 470px; }
  .blurb {
    position: absolute;
    left: 0;
    width: 100%;
    text-align: center;
    font-family: "Libre Baskerville", serif;
    font-weight: 700;
    font-size: 19px;
    line-height: 34px;
    color: var(--body-blue);
  }
  .blurb.first { top: 395px; }
  .blurb.second { top: 532px; }
  .street-scene {
    position: absolute;
    left: 0;
    bottom: 0;
    width: 100%;
    height: 340px;
    background: linear-gradient(
      180deg,
      rgba(230, 242, 247, 0) 0%,
      var(--scene-sky) 18%,
      var(--scene-roof) 32%,
      var(--scene-wall) 55%,
      var(--scene-tree) 80%,
      var(--scene-ground) 100%
    );
  }
</style>
</head>
<body>
  <main class="poster">
    <h1 class="poster-title">
      <span class="name">ASHCOMBE</span>
      <span class="tagline">Veterans Village</span>
    </h1>

    <div class="rule top"></div>
    <p class="blurb first">Lorem ipsum dolor sit amet,<br>consectetuer adipiscing elit, volutpat.</p>
    <div class="rule bottom"></div>

    <p class="blurb second">Lorem ipsum dolor sit amet,<br>consectetuer adipiscing elit, volutpat.</p>

    <div class="street-scene" role="img" aria-label="Architectural rendering of craftsman-style two-storey townhomes with gabled roofs and street trees along a sidewalk"></div>
  </main>
</body>
</html>
```